Factory Beam Works

We manufacture and distribute luminaires for industrial lighting applications. We cover the European market. We look for a basic well designed web site, with not too much text, as we're gonna do it multilingual. Requirements: a.) Wordpress Avada Theme b.) Pages: 1. Start (compare http://www.brivantel.co.kr/rb/?r=en and www.morvack.de for slides => mixed products & industry photos) 2. Company (short description) http://www.morvack.de/en/company/about-us, european map with offices in Stockholm (Sweden), Berlin Heidelberg (Germany), Linz (Austria) Description fill in : "The name of FBW stands for competence and quality in all areas of technical light fittings: waterproof / dustproof light fittings - industrial-grade light fittings - outdoor luminaires - A very high level of reliability, of competence and innovation their mark on thinking and actions of people working in the family company. FBW for a very long time: research and development, laboratory work, toolmaking, polyester pressing plant, sheet metal forming, powder coating and assembly are concentrated in FBW's own premises. Worldwide innovations have helped FBW over and over again to launch new impulses to the market. For decades now FBW has been one of the leading bidders of this industrial sector. The international significance of FBW as a lighting specialist is based on intelligent and useful solutions - not just with respect to standard products but as far as branch-specific technical problems or application conditions and particular customer wishes are concerned. "3. Products [pls. see infographic under https://www.quendora.com/en/applications/industry/lighting-for-industry/ [we are looking for something similar to start on top, then short description product with download pdf] 4. News (Events, new products, etc.) 5. Partner login (for downloads of further data, well structured) 6. Contact (4 office adresses, map, no contact form) c.) Logo / Colors: 1 Logo with 2 different colors, please choose either blue or red one or the colors according to your recommendation d.) What do we do? High quality industrial lighting smart lighting control e.) Industries: Look at this photo here for a glimpse: http://www.pelmarot-werk.de/lichttechnik f.) Areas: Look at the infographic here, to get an idea which areas of lighting / products we are covering: https://www.quendora.com/en/applications/industry/lighting-for-industry/ => Design / Associations: Fresh, clear, technology, high quality, solidity, reliability experience like https://www.quendora.com/en/applications/industry/lighting-for-industry/ Thank you very much for your offers!

Target Market(s)

Resellers / Wholesalers of industrial luminaires AND direct clients (industrial, commercial)

Industry/Entity Type

Light Industrial

Coding

Coded - Design and coding required

Number of Pages Required

5+ page

Font styles to use
Sans Serif

Colors
0355a3
ec1f27

Requirements
Must have
• a.) Wordpress Avada Theme b.) Pages: 1. Start / 2. Company (short description, european map with offices in Stockholm (Sweden), Berlin Heidelberg (Germany), Linz (Austria) / 3. Products [pls infographic under f.) => News (Events, new products, etc.) / 5. Partner Login (for Downloads) / 6. Contact c.) Logo / Colors: 1 Logo with 2 different colors, please choose either blue or red one or the colors according to your recommendation d.) What do we do? High quality industrial lighting smart lighting control e.) Industries: Look at this photo here for a glimpse: http://www.pelmarot-werk.de/lichttechnik f.) Areas: Look at the infographic here, to get an idea which areas of lighting / products we are covering: https: //www.quendora. com / en / applications / industry / lighting-for-industry / => Design / Associations: Fresh, clear, technology, high quality, solidity, reliability experience => tidy look
Nice to have
• - some nice WP Avada elements - map with locations (see b.) 2.) above) - infographic (see f.) above)
Should not have
• not too overloaded, not too crowded

```html
<!DOCTYPE html>
<html lang="en">
<head>
<meta charset="utf-8">
<title>Factory Beam Works — Home</title>
<link rel="stylesheet" href="https://fonts.googleapis.com/css2?family=Montserrat:wght@300;400;500;600;700&display=swap">
<style>
:root{
  --red:#ec1f27;
  --ink:#111111;
  --header:#1d1d1d;
  --footer:#1b1b1b;
  --bottom:#0c0c0c;
  --page:#f4f4f4;
  --white:#ffffff;
  --text:#222222;
  --line:#4a4a4a;
  --partner-blue:#2f8ff0;
  --partner-pink:#ee2bd2;
  --partner-green:#3ee35a;
  --partner-yellow:#f3ee2b;
}
*{box-sizing:border-box;margin:0;padding:0}
html,body{width:1200px;height:1200px;overflow:hidden;background:var(--page);font-family:'Montserrat',sans-serif}
.site{position:absolute;left:39px;top:0;width:1076px;height:1150px;transform:scale(1.0435);transform-origin:0 0;background:var(--white);box-shadow:0 6px 18px rgba(0,0,0,.12)}
.abs{position:absolute}

.topbar{left:0;top:0;width:1076px;height:30px;background:var(--ink);color:#bbb;font-size:8px}
.topbar .lang-label{left:95px;top:10px}
.lang-select{left:182px;top:5px;width:91px;height:19px;border:1px solid #555;color:var(--red);font-size:8px;padding:4px 0 0 14px}
.lang-select .caret{position:absolute;right:0;top:0;width:20px;height:17px;border-left:1px solid #555}
.lang-select .caret svg{margin:5px 0 0 5px}
.follow{left:710px;top:11px;letter-spacing:.3px;color:#ccc}
.social{left:836px;top:0;display:flex}
.social span{width:32px;height:30px;border-left:1px solid #333;display:flex;align-items:center;justify-content:center}
.social span i{width:7px;height:7px;background:var(--red);border-radius:50%;display:block}

.header{left:0;top:30px;width:1076px;height:73px;background:var(--header)}
.brand{left:78px;top:23px;display:flex;align-items:center;gap:6px;color:var(--red);font-weight:700;font-size:13px;letter-spacing:.3px;white-space:nowrap}
.brand i{width:14px;height:14px;background:var(--red);display:block;flex:none}
.nav{left:281px;top:30px;display:flex;gap:0;font-size:11.5px;font-weight:600;color:var(--white)}
.nav a{color:inherit;text-decoration:none;margin-right:29px}
.nav a.active{color:var(--red)}
.search{left:775px;top:18px;width:222px;height:38px;border:1px solid #555;color:var(--white);font-size:11.5px;font-weight:600;padding:12px 0 0 12px}
.search .btn{position:absolute;right:0;top:0;width:38px;height:36px;border-left:1px solid #555;display:flex;align-items:center;justify-content:center}

.hero{left:0;top:103px;width:1076px;height:344px;background:linear-gradient(160deg,#9a9fa3 0%,#54585c 35%,#2f3236 65%,#6a5a3a 100%)}
.hero-panel{left:514px;top:77px;width:483px;height:267px;background:rgba(30,30,30,.45);border-top:6px solid var(--red);color:var(--white)}
.hero-panel h1{position:absolute;left:33px;top:37px;font-weight:300;font-size:25px}
.hero-panel p{position:absolute;left:34px;top:84px;width:412px;font-size:10.5px;line-height:13.5px}
.dots{left:904px;top:318px;display:flex;gap:7px}
.dots i{width:7px;height:7px;border:1.5px solid #fff;border-radius:50%;display:block}

.support{left:80px;top:459px;width:175px;height:352px;background:var(--red);color:var(--white)}
.support h2{position:absolute;left:11px;top:9px;font-size:12.5px;font-weight:700}
.support .intro{position:absolute;left:0;top:42px;width:175px;text-align:center;font-size:9.5px;font-weight:600;line-height:12.5px}
.support .box{position:absolute;left:16px;width:145px;height:70px;border:1px solid var(--white);text-align:center}
.support .call{top:102px}
.support .call small{display:block;font-size:7.5px;margin-top:11px}
.support .call b{display:block;font-size:20px;font-weight:400;margin-top:2px}
.support .chat{top:183px;font-size:13px;font-weight:600;padding-top:27px}
.support .mail{top:267px;font-size:13px;font-weight:600;padding-top:28px}

.card{top:459px;width:236px;height:352px;background:var(--white);box-shadow:0 1px 6px rgba(0,0,0,.18)}
.card h2{position:absolute;left:9px;top:7px;color:var(--red);font-size:12.5px;font-weight:700}
.card .media{position:absolute;left:0;top:32px;width:236px;height:127px}
.card h3{position:absolute;left:18px;top:173px;width:200px;font-size:12.5px;font-weight:700;line-height:16px;color:var(--text)}
.card p{position:absolute;left:18px;width:202px;font-size:8.6px;line-height:10.7px;color:var(--text)}
.card .more{position:absolute;left:0;bottom:0;width:236px;height:31px;background:var(--red);color:var(--white);font-size:10.5px;font-weight:600;text-align:center;padding-top:9px}

.footer{left:0;top:825px;width:1076px;height:216px;background:var(--footer);color:var(--white)}
.footer h4{position:absolute;top:20px;color:var(--red);font-size:12.5px;font-weight:700}
.footer .rule{position:absolute;left:80px;top:56px;width:917px;height:1px;background:var(--line)}
.footer ul{position:absolute;list-style:none;font-size:11.5px;font-weight:500;line-height:18px}
.footer ul.tight{line-height:14.5px}
.footer .phone{position:absolute;left:840px;top:84px;font-size:18px;font-weight:500}
.footer .hours{position:absolute;left:843px;top:109px;font-size:7.5px;line-height:9.5px}
.footer .chat24{position:absolute;left:843px;top:156px;width:129px;height:30px;border:1px solid var(--red);color:var(--red);font-size:7.5px;font-weight:600;padding:10px 0 0 51px}
.footer .chat24 svg{position:absolute;left:13px;top:7px}

.bottom{left:0;top:1041px;width:1076px;height:109px;background:var(--bottom);color:var(--white)}
.bottom .brand{left:80px;top:42px;font-size:10.5px;gap:5px;letter-spacing:0}
.bottom .brand i{width:11px;height:11px}
.address{left:231px;top:34px;font-size:10px;font-weight:500;line-height:12.8px}
.partners-label{left:628px;top:47px;font-size:10px;font-weight:600}
.partner{top:34px;width:53px;height:34px;border-radius:3px}
.partner-name{top:81px;width:53px;text-align:center;font-size:6.5px;font-weight:600}
</style>
</head>
<body>
<div class="site">

  <div class="abs topbar">
    <span class="abs lang-label">Select Language</span>
    <div class="abs lang-select">English<span class="caret"><svg width="9" height="6" viewBox="0 0 9 6"><path d="M1 1l3.5 3.5L8 1" fill="none" stroke="#ec1f27" stroke-width="1.4"/></svg></span></div>
    <span class="abs follow">FOLLOW US ON SOCIAL</span>
    <div class="abs social"><span><i></i></span><span><i></i></span><span><i></i></span><span><i></i></span><span><i></i></span></div>
  </div>

  <header class="abs header">
    <div class="abs brand"><i></i>Factory Beam Works</div>
    <nav class="abs nav">
      <a class="active">HOME</a><a>COMPANY</a><a>PRODUCTS</a><a>NEWS</a><a>PARTNER</a><a>CONTACT</a>
    </nav>
    <div class="abs search">Search
      <span class="btn"><svg width="13" height="13" viewBox="0 0 13 13"><circle cx="5.3" cy="5.3" r="4" fill="none" stroke="#fff" stroke-width="1.8"/><path d="M8.3 8.3L12 12" stroke="#fff" stroke-width="2"/></svg></span>
    </div>
  </header>

  <section class="abs hero" role="img" aria-label="Interior of a large factory hall with roof skylights and rows of high bay lamps">
    <div class="abs hero-panel">
      <h1>Experience builds trust.</h1>
      <p>Lorem ipsum dolor sit amet, consectetur adipiscing elit, sed do eiusmod tempor incididunt ut labore et dolore magna aliqua. Ut enim ad minim veniam, quis nostrud exercitation ullamco laboris nisi ut aliquip ex ea commodo consequat. Duis aute irure dolor in reprehenderit in voluptate velit esse cillum dolore eu fugiat nulla pariatur.</p>
    </div>
    <div class="abs dots"><i></i><i></i><i></i><i></i><i></i></div>
  </section>

  <aside class="abs support">
    <h2>SUPPORT</h2>
    <div class="intro">Have Questions?<br>We have answer.<br>Get in touch with us today!</div>
    <div class="box call"><small>Call Us</small><b>000-111-1234</b></div>
    <div class="box chat">Chat with us</div>
    <div class="box mail">Send Us E-Mail</div>
  </aside>

  <article class="abs card" style="left:266px">
    <h2>NEWS</h2>
    <div class="media" role="img" aria-label="Black floodlight luminaire glowing on a pole" style="background:linear-gradient(135deg,#ffffff 20%,#e8dcc0 45%,#6b6b6b 70%,#ffffff 90%)"></div>
    <h3>FBW 001 WIDE ANGLE LIGHTNING COMMERCIAL LED</h3>
    <p style="top:234px">Lorem ipsum dolor sit amet, consectetur adipiscing elit, sed do eiusmod tempor incididunt ut labore et dolore magna aliqua. Ut enim ad minim veniam, quis nostrud exercitation ullamco laboris nisi ut aliquip ex ea commodo consequat. Duis aute irure dolor in reprehenderit in voluptate ...</p>
    <div class="more">More</div>
  </article>

  <article class="abs card" style="left:513px">
    <h2>PRODUCTS</h2>
    <div class="media" role="img" aria-label="Round UFO high bay LED lamp" style="background:linear-gradient(180deg,#ffffff 0%,#d9dbe0 45%,#9aa0b4 70%,#ffffff 95%)"></div>
    <h3>300W UFO High Bay Light LED Industrial Lamp</h3>
    <p style="top:224px">Lorem ipsum dolor sit amet, consectetur adipiscing elit, sed do eiusmod tempor incididunt ut labore et dolore magna aliqua. Ut enim ad minim veniam, quis nostrud exercitation ullamco laboris nisi ut aliquip ex ea commodo consequat. Duis aute irure dolor in reprehenderit in voluptate ...</p>
    <div class="more">More</div>
  </article>

  <article class="abs card" style="left:760px">
    <h2>APPLICATIONS</h2>
    <div class="media" role="img" aria-label="Open plan office with desks and ceiling lights" style="background:linear-gradient(180deg,#e9eef2 0%,#b8c2ca 50%,#6f7a84 100%)"></div>
    <h3>OFFICE BUILDING</h3>
    <p style="top:202px">Lorem ipsum dolor sit amet, consectetur adipiscing elit, sed do eiusmod tempor incididunt ut labore et dolore magna aliqua. Ut enim ad minim veniam, quis nostrud exercitation ullamco laboris nisi ut aliquip ex ea commodo consequat. Duis aute irure dolor in reprehenderit in voluptate sed do eiusmod tempor incididunt ut labore et dolore magna aliqua. Ut enim ad minim veniam, quis nostrud exercitation ...</p>
    <div class="more">More</div>
  </article>

  <footer class="abs footer">
    <h4 style="left:117px">PRODUCT</h4>
    <h4 style="left:298px">APPLICATIONS</h4>
    <h4 style="left:482px">SERVICE</h4>
    <h4 style="left:666px">COMPANY</h4>
    <h4 style="left:840px">CONTACT</h4>
    <div class="rule"></div>
    <ul style="left:113px;top:70px"><li>Industrial Lighting</li><li>Outdoor Lighting</li><li>Indoor Lighting</li><li>Lamp</li><li>Engine</li><li>References</li></ul>
    <ul style="left:298px;top:70px"><li>Office</li><li>Industry</li><li>Health &amp; Care</li><li>Education</li><li>Outdoor</li><li>Shop &amp; Retail</li><li>Architectural</li></ul>
    <ul style="left:482px;top:67px"><li style="line-height:14.5px">Downloads</li><li style="line-height:14.5px">After-sales policy</li><li>Light Services</li><li>Knowledge</li></ul>
    <ul class="tight" style="left:666px;top:67px"><li>Partner</li><li>Office Locations</li><li>Career</li><li>Events</li><li>Company Profile</li><li>CEO</li></ul>
    <div class="phone">000-111-1234</div>
    <div class="hours">Monday- Sunday,<br>8: 00-18: 00<br>(calls only)</div>
    <div class="chat24"><svg width="20" height="15" viewBox="0 0 20 15"><ellipse cx="7" cy="6" rx="6.5" ry="5" fill="#ec1f27"/><ellipse cx="13" cy="9" rx="6" ry="4.6" fill="#ec1f27"/></svg>Chat 24 hours</div>
  </footer>

  <div class="abs bottom">
    <div class="abs brand"><i></i>Factory Beam Works</div>
    <div class="abs address">1234 Some street, Region, province, Country 12000<br>TEL. 000-111-1234 &nbsp;&nbsp; FAX. 000-111-1234<br>Copyright (C) 2016 Brivantel. All Rights Reserved.</div>
    <span class="abs partners-label">OUR PARTNERS</span>
    <div class="abs partner" style="left:746px;background:var(--partner-blue)"></div>
    <div class="abs partner" style="left:812px;background:var(--partner-pink)"></div>
    <div class="abs partner" style="left:878px;background:var(--partner-green)"></div>
    <div class="abs partner" style="left:944px;background:var(--partner-yellow)"></div>
    <span class="abs partner-name" style="left:746px">COMPANY 1</span>
    <span class="abs partner-name" style="left:812px">COMPANY 2</span>
    <span class="abs partner-name" style="left:878px">COMPANY 3</span>
    <span class="abs partner-name" style="left:944px">COMPANY 4</span>
  </div>

</div>
</body>
</html>
```